Leaf Haven Business Card Design

My E-Commerce store is called Leaf Haven

Website address is - http://www.leafhaven-demo.com.au

I would like a colourful, friendly business with the description in the 'must haves' box incorporated into it
Updates

Please add the following to the business cards; Natural & Organic Products Online Organic Pantry Items Superfoods & Supplements Natural Skincare Eco Friendly Household Products

Industry/Entity Type

Business

Contact Information for Business Card

www.leafhaven-demo.com.au
mira@leafhaven-demo.com.au

Colors
acd037
9bcb3c
cadf82
eaf2ce

Requirements
Must have
• Natural & Organic Eco Products Online.
• Leaf Haven specialises in organic pantry items, superfoods and supplements, organic skincare for you and your family & eco friendly household products.

```html
<!DOCTYPE html>
<html lang="en">
<head>
<meta charset="utf-8">
<title>Leaf Haven Business Card</title>
<link rel="stylesheet" href="https://fonts.googleapis.com/css2?family=Open+Sans:wght@400;600;700&display=swap">
<style>
  :root {
    --bg: #e6e8e6;
    --card: #ffffff;
    --ink: #2b2b2b;
    --ink-soft: #555555;
    --green-deep: #1fae5a;
    --green: #3cc46e;
    --green-light: #8fe0a6;
    --panel-edge: #dcdcdc;
  }
  * { margin: 0; padding: 0; box-sizing: border-box; }
  html, body { width: 1200px; height: 957px; overflow: hidden; }
  body {
    background: var(--bg);
    font-family: "Open Sans", Arial, sans-serif;
    position: relative;
  }
  .card {
    position: absolute;
    left: 220px;
    width: 760px;
    height: 434px;
    background: var(--card);
    box-shadow: 0 6px 18px rgba(0,0,0,.18);
    overflow: hidden;
  }
  .card--back { top: 36px; }
  .card--front { top: 490px; }

  .brand {
    position: absolute;
    display: flex;
    align-items: center;
    gap: 16px;
  }
  .brand__dot {
    width: 42px; height: 42px;
    border-radius: 50%;
    background: var(--green);
    flex: none;
  }
  .brand__name {
    font-weight: 600;
    font-size: 44px;
    color: var(--green-deep);
    letter-spacing: .5px;
    white-space: nowrap;
  }

  .card--back .brand { left: 50%; top: 78px; transform: translateX(-50%); }
  .back__tagline {
    position: absolute;
    left: 0; right: 0; top: 160px;
    text-align: center;
    font-size: 18px;
    font-weight: 600;
    color: var(--green-deep);
  }
  .back__products {
    position: absolute;
    left: 80px; right: 80px; top: 202px;
    display: flex;
    flex-wrap: wrap;
    justify-content: center;
    gap: 8px 22px;
    list-style: none;
    font-size: 15px;
    color: var(--ink-soft);
  }
  .back__products li { display: flex; align-items: center; gap: 8px; }
  .back__products li::before {
    content: "";
    width: 7px; height: 7px;
    border-radius: 50%;
    background: var(--green);
  }
  .back__url {
    position: absolute;
    left: 0; right: 0; top: 330px;
    text-align: center;
    font-size: 22px;
    font-weight: 600;
    letter-spacing: 2px;
    color: var(--ink);
  }

  .card--front .brand { left: 46px; top: 186px; }
  .card--front .brand__name { font-size: 38px; }
  .card--front .brand__dot { width: 38px; height: 38px; }
  .front__art { position: absolute; inset: 0; }

  .contact {
    position: absolute;
    left: 442px;
    top: 60px;
    color: var(--ink);
  }
  .contact__name { font-size: 24px; font-weight: 700; line-height: 1.1; }
  .contact__title { font-size: 18px; color: var(--green); margin-bottom: 12px; }
  .contact__list { list-style: none; font-size: 15px; color: var(--ink-soft); }
  .contact__list li { display: flex; align-items: center; gap: 10px; height: 26px; }
  .contact__list svg { width: 15px; height: 15px; fill: var(--green); flex: none; }
  .contact__address { margin-top: 14px; font-size: 15px; color: var(--ink-soft); line-height: 1.55; }
</style>
</head>
<body>

<section class="card card--back">
  <div class="brand">
    <span class="brand__dot"></span>
    <span class="brand__name">Leaf Haven</span>
  </div>
  <p class="back__tagline">Natural &amp; Organic Eco Products Online</p>
  <ul class="back__products">
    <li>Organic Pantry Items</li>
    <li>Superfoods &amp; Supplements</li>
    <li>Natural Skincare</li>
    <li>Eco Friendly Household Products</li>
  </ul>
  <p class="back__url">www.leafhaven-demo.com.au</p>
</section>

<section class="card card--front">
  <svg class="front__art" viewBox="0 0 760 434" aria-hidden="true">
    <defs>
      <filter id="panelShadow" x="-10%" y="-10%" width="120%" height="130%">
        <feDropShadow dx="-2" dy="3" stdDeviation="4" flood-opacity=".18"/>
      </filter>
    </defs>
    <polygon points="412,30 760,30 760,300 400,368" fill="#ffffff" stroke="var(--panel-edge)" filter="url(#panelShadow)"/>
    <polygon points="470,434 760,330 760,434" fill="var(--green-light)"/>
    <polygon points="0,412 560,412 760,360 760,434 0,434" fill="var(--green)"/>
    <polygon points="0,422 760,422 760,434 0,434" fill="var(--green-deep)"/>
  </svg>

  <div class="brand">
    <span class="brand__dot"></span>
    <span class="brand__name">Leaf Haven</span>
  </div>

  <div class="contact">
    <p class="contact__name">Your Name</p>
    <p class="contact__title">Title</p>
    <ul class="contact__list">
      <li>
        <svg viewBox="0 0 24 24"><path d="M6.6 10.8a15.1 15.1 0 0 0 6.6 6.6l2.2-2.2c.3-.3.7-.4 1-.2 1.1.4 2.3.6 3.6.6.6 0 1 .4 1 1V20c0 .6-.4 1-1 1A17 17 0 0 1 3 4c0-.6.4-1 1-1h3.5c.6 0 1 .4 1 1 0 1.300.2 2.5.6 3.6.1.3 0 .7-.2 1z"/></svg>
        012-345-6789
      </li>
      <li>
        <svg viewBox="0 0 24 24"><path d="M2 5h20v14H2z M4 7v.5l8 5 8-5V7l-8 5z" fill-rule="evenodd"/></svg>
        mira@leafhaven-demo.com.au
      </li>
      <li>
        <svg viewBox="0 0 24 24"><path d="M12 2a10 10 0 1 0 0 20 10 10 0 0 0 0-20zm6.9 6h-3a15 15 0 0 0-1.3-3.9A8 8 0 0 1 18.9 8zM12 4c.8 1.2 1.5 2.5 1.9 4h-3.8c.4-1.5 1.1-2.8 1.9-4zM4.3 14a8 8 0 0 1 0-4h3.4a16 16 0 0 0 0 4zm.8 2h3a15 15 0 0 0 1.3 3.9A8 8 0 0 1 5.1 16zm3-8h-3a8 8 0 0 1 4.3-3.9C8.8 5.3 8.4 6.6 8.1 8zM12 20c-.8-1.2-1.5-2.5-1.900-4h3.8c-.4 1.5-1.1 2.8-1.9 4zm2.3-6H9.7a14 14 0 0 1 0-4h4.6a14 14 0 0 1 0 4zm.3 5.9c.6-1.2 1-2.5 1.3-3.9h3a8 8 0 0 1-4.3 3.9zm1.7-5.9a16 16 0 0 0 0-4h3.4a8 8 0 0 1 0 4z"/></svg>
        www.leafhaven-demo.com.au
      </li>
    </ul>
    <p class="contact__address">Street Name, City Name<br>Zipcode-012345</p>
  </div>
</section>

</body>
</html>
```